Brinevale Yacht Management Full Page Ad Flyer

Yacht Management Package also includes the following periodic Monthly services:

Monthly full vessel systems checklist inspections
Diver For Hull Cleaning And Inspection Of Props, Shafts, and Zincs
Interior/Exterior Detailing and scheduled washdowns
Manage Haulout
Pump-out Services
On-call Captain and Crew Services
Updates

Need more time to provide more content to designers and the printing press template file.

Target Market(s)

Vessel owners, motor yachts, sailboats from 25 feet in length up to 125 feet in length. We do not do cruise ships or yachts larger than 125 feet. Someone who has their boat docked at their house or a local marina. We also offer mobile on-site services.

```html
<!DOCTYPE html>
<html lang="en">
<head>
<meta charset="utf-8">
<title>Brinevale Yacht Management – Full Page Flyer</title>
<link rel="stylesheet" href="https://fonts.googleapis.com/css2?family=Montserrat:wght@400;500;800&display=swap">
<style>
  :root {
    --stage: #000000;
    --paper: #ffffff;
    --brand-blue: #1f56a0;
    --brand-ink: #2c4f8c;
    --heading-slate: #5e8190;
    --body-ink: #2b2b2b;
    --accent-teal: #5f8f9c;
    --mist-top: #f4f6f8;
    --mist-mid: #dfe6ec;
    --mist-low: #cbd7e0;
    --sea-sky: #9fb3c6;
    --sea-mid: #6f859b;
    --sea-deep: #1f3a57;
  }
  * { margin: 0; padding: 0; box-sizing: border-box; }
  html, body {
    width: 1200px; height: 1200px; overflow: hidden;
    background: var(--stage);
    font-family: "Montserrat", Arial, sans-serif;
  }
  .flyer {
    position: absolute; left: 234px; top: 83px;
    width: 731px; height: 1034px;
    background: var(--paper); overflow: hidden;
  }
  .flyer__art { position: absolute; inset: 0; width: 731px; height: 1034px; }
  .brand {
    position: absolute; left: 57px; top: 114px;
    color: var(--brand-ink); font-weight: 500;
    text-align: center; line-height: 1;
  }
  .brand__name { display: block; font-size: 44px; letter-spacing: 5px; }
  .brand__sub { display: block; font-size: 11px; letter-spacing: 7px; margin-top: 4px; }
  .headline {
    position: absolute; left: 47px; top: 316px;
    color: var(--heading-slate); font-weight: 800;
    font-size: 31px; line-height: 37px; text-transform: uppercase;
    white-space: nowrap;
  }
  .headline span { display: block; }
  .services {
    position: absolute; left: 47px; top: 496px;
    list-style: none; color: var(--body-ink);
    font-size: 18px; line-height: 31px; font-weight: 400;
  }
  .services li { display: flex; align-items: center; gap: 9px; white-space: nowrap; }
  .services svg { width: 9px; height: 11px; flex: none; }
</style>
</head>
<body>
  <main class="flyer">
    <svg class="flyer__art" viewBox="0 0 731 1034">
      <defs>
        <linearGradient id="mistGradient" x1="0" y1="0" x2="0" y2="1">
          <stop offset="0" stop-color="var(--mist-top)"/>
          <stop offset="0.5" stop-color="var(--mist-mid)"/>
          <stop offset="1" stop-color="var(--mist-low)"/>
        </linearGradient>
        <linearGradient id="seaGradient" x1="0" y1="0" x2="0" y2="1">
          <stop offset="0" stop-color="var(--sea-sky)"/>
          <stop offset="0.45" stop-color="var(--sea-mid)"/>
          <stop offset="1" stop-color="var(--sea-deep)"/>
        </linearGradient>
      </defs>
      <rect class="backdrop-photo" x="0" y="180" width="731" height="720" fill="url(#mistGradient)"
            role="img" aria-label="Faded photo of a yacht tender moored near a rocky shore"/>
      <path class="hero-photo" d="M0,880 C240,810 500,760 731,740 V1034 H0 Z" fill="url(#seaGradient)"
            role="img" aria-label="Photo of a dark motor yacht cruising at speed on open sea"/>
      <path class="band band--teal"
            d="M0,866 C240,796 500,746 731,726 L731,744 C500,764 240,814 0,882 Z"
            fill="var(--accent-teal)"/>
      <path class="header-panel" d="M0,0 H731 V150 C520,215 260,235 0,222 Z" fill="var(--paper)"/>
      <path class="band band--blue"
            d="M0,218 C260,232 520,210 731,146 L731,162 C520,226 260,244 0,228 Z"
            fill="var(--brand-blue)"/>
    </svg>

    <div class="brand">
      <span class="brand__name">BRINEVALE</span>
      <span class="brand__sub">YACHT MANAGEMENT</span>
    </div>

    <h1 class="headline">
      <span>Yacht management package</span>
      <span>also includes the following</span>
      <span>periodic monthly services:</span>
    </h1>

    <ul class="services">
      <li><svg viewBox="0 0 9 11"><path d="M1.5,1 L6.5,5.5 L1.5,10" fill="none" stroke="currentColor" stroke-width="2.6"/></svg>Monthly full vessel systems checklist inspections</li>
      <li><svg viewBox="0 0 9 11"><path d="M1.5,1 L6.5,5.5 L1.5,10" fill="none" stroke="currentColor" stroke-width="2.6"/></svg>Diver For Hull Cleaning And Inspection Of Props, Shafts, and Zincs</li>
      <li><svg viewBox="0 0 9 11"><path d="M1.5,1 L6.5,5.5 L1.5,10" fill="none" stroke="currentColor" stroke-width="2.6"/></svg>Interior/Exterior Detailing and scheduled washdowns</li>
      <li><svg viewBox="0 0 9 11"><path d="M1.5,1 L6.5,5.5 L1.5,10" fill="none" stroke="currentColor" stroke-width="2.6"/></svg>Manage Haulout</li>
      <li><svg viewBox="0 0 9 11"><path d="M1.5,1 L6.5,5.5 L1.5,10" fill="none" stroke="currentColor" stroke-width="2.6"/></svg>Pump-out Services</li>
      <li><svg viewBox="0 0 9 11"><path d="M1.5,1 L6.5,5.5 L1.5,10" fill="none" stroke="currentColor" stroke-width="2.6"/></svg>On-call Captain and Crew Services</li>
    </ul>
  </main>
</body>
</html>
```